Bedrock Yield Private Holdings Scheme

I want a professional design for a new investment program that we have designed for prospecting new prospects. We have a company logo and the content that we would like for the brochure but we would like and design structure and graphics to help compliment the content. I am attaching a rough draft of the brochure that has some

Target Market(s)

Anyone looking for hard assets, inflation hedge, cash flow investments.

```html
<!DOCTYPE html>
<html lang="en">
<head>
<meta charset="utf-8">
<title>Bedrock Yield Private Holdings Scheme — Brochure</title>
<link href="https://fonts.googleapis.com/css2?family=Open+Sans:wght@400;600;700&display=swap" rel="stylesheet">
<style>
  :root{
    --green:#2f6d35;
    --green-dark:#1f5226;
    --green-light:#a8c99f;
    --green-pale:#d9e8d3;
    --charcoal:#585a5b;
    --charcoal-dark:#474849;
    --ink:#3a3a3a;
    --muted:#6d6d6d;
    --paper:#ffffff;
    --ground:#e4e4e3;
  }
  *{box-sizing:border-box;margin:0;padding:0}
  html,body{width:1200px;height:2540px;overflow:hidden}
  body{background:var(--ground);font-family:"Open Sans",Arial,sans-serif;color:var(--ink);position:relative}
  .page{position:absolute;width:560px;height:725px;background:var(--paper);overflow:hidden;box-shadow:0 2px 10px rgba(0,0,0,.12)}
  .page svg.shapes{position:absolute;inset:0}
  .cover-front{left:320px;top:80px}
  .outer-back{left:40px;top:895px}
  .outer-front{left:600px;top:895px}
  .inner-left{left:40px;top:1710px}
  .inner-right{left:600px;top:1710px}

  .title{position:absolute;left:40px;top:38px;font-family:"Open Sans",Arial,sans-serif;font-weight:600;color:#fff;font-size:20px;letter-spacing:.3px}
  .photo{position:absolute}
  .photo-oilfield{left:0;top:112px;width:560px;height:440px;
    background:linear-gradient(180deg,#3f7fc4 0%,#7fb0df 38%,#dfe6ee 52%,#7f88a0 58%,#b69a68 66%,#a78652 100%);
    clip-path:polygon(0 6%,100% 0,100% 94%,0 100%)}
  .brand{position:absolute;display:flex;align-items:center;gap:8px}
  .brand-dot{width:16px;height:16px;border-radius:50%;background:var(--green);flex:none}
  .brand-name{font-family:"Open Sans",Arial,sans-serif;font-weight:600;color:var(--green);font-size:19px;line-height:1.15}
  .cover-note{position:absolute;right:28px;top:585px;width:250px;font-size:7.5px;line-height:1.45;color:var(--green)}
  .cover-note p+p{margin-top:6px}
  .url-tab{position:absolute;right:0;bottom:24px;height:36px;width:280px;background:var(--green);border-top-left-radius:30px;color:#fff;font-size:11px;font-weight:600;display:flex;align-items:center;justify-content:flex-end;padding-right:26px}

  /* back cover */
  .work-heading{position:absolute;left:34px;top:205px;width:110px;color:#e8e8e8;font-size:14px;line-height:1.3}
  .steps{position:absolute;left:170px;top:92px;width:372px;list-style:none}
  .step{display:flex;align-items:center;height:66px;margin-bottom:8px;position:relative}
  .step-icon{width:42px;height:42px;border-radius:50%;background:#fff;border:3px solid var(--green-light);flex:none;z-index:2;display:flex;align-items:center;justify-content:center}
  .step-pill{margin-left:-18px;padding:7px 14px 7px 26px;background:var(--green-dark);border-radius:0 30px 30px 0;flex:1;color:#fff}
  .step-pill h4{font-size:9px;font-weight:700;letter-spacing:.6px;text-transform:uppercase;margin-bottom:2px}
  .step-pill p{font-size:7px;line-height:1.35;color:#dbe7d8}
  .contact{position:absolute;left:190px;top:585px;list-style:none;font-size:9px;color:var(--ink)}
  .contact li{display:flex;align-items:center;gap:8px;height:18px}
  .contact svg{width:11px;height:11px;flex:none}

  /* inner spread */
  .lead{position:absolute;left:28px;top:30px;width:505px;color:#fff}
  .lead h2{font-size:13px;font-weight:700;line-height:1.35}
  .lead h3{font-size:10px;font-weight:600;color:var(--green-light);margin-top:6px}
  .lead p{font-size:7.5px;line-height:1.5;color:#e3e3e3;margin-top:10px}
  .intro{position:absolute;left:28px;top:262px;width:505px;font-size:7.5px;line-height:1.5;color:var(--muted)}
  .col{position:absolute;top:320px;width:240px}
  .col-a{left:28px}.col-b{left:292px}
  .col-head{background:var(--green);color:#fff;font-size:9px;font-weight:700;padding:6px 10px 6px 30px;border-radius:0 16px 16px 0;position:relative}
  .col-head::before{content:"";position:absolute;left:6px;top:50%;width:16px;height:16px;margin-top:-8px;border-radius:50%;background:#fff}
  .bullets{list-style:none;margin-top:8px}
  .bullets li{font-size:7px;line-height:1.45;color:var(--muted);padding-left:12px;position:relative;margin-bottom:5px}
  .bullets li::before{content:"";position:absolute;left:0;top:3px;width:5px;height:5px;border-radius:50%;background:var(--green)}
  .photo-coins{left:0;bottom:0;width:560px;height:190px;background:linear-gradient(180deg,#ffffff 0%,#f1ede3 40%,#c9a45a 75%,#8a6a2e 100%)}
  .photo-markets{left:0;top:0;width:560px;height:235px;background:linear-gradient(160deg,#eef1f4 0%,#c7ccd1 40%,#d7b46a 70%,#9c7a38 100%)}
  .why{position:absolute;left:40px;width:490px}
  .why h3{font-size:10px;font-weight:700;color:var(--green);margin-bottom:7px}
  .why-1{top:322px}.why-2{top:455px}
  .why .bullets li{font-size:7.5px}
</style>
</head>
<body>

<!-- Front cover -->
<section class="page cover-front">
  <svg class="shapes" width="560" height="725" viewBox="0 0 560 725">
    <polygon points="0,0 560,0 560,92 0,118" fill="var(--green)"/>
    <polygon points="0,118 560,92 560,100 0,126" fill="var(--green-light)"/>
    <polygon points="0,552 560,545 560,552 0,562" fill="var(--green-light)"/>
    <path d="M0,562 L200,558 Q225,558 235,572 L0,578 Z" fill="var(--green)"/>
  </svg>
  <h1 class="title">Bedrock Yield Private Holdings Scheme</h1>
  <div class="photo photo-oilfield" role="img" aria-label="Photo of an oil pump jack in a dry field with snowy mountains under a blue sky"></div>
  <div class="brand" style="left:34px;top:630px"><span class="brand-dot"></span><span class="brand-name">Bedrock Yield, LLC</span></div>
  <div class="cover-note">
    <p>What should investors do in this uncertain period to profit from the evolving energy transition and protect themselves from what appears to be an inevitable wave of inflation?</p>
    <p>We have one asset class and a business opportunity that can address both.</p>
  </div>
  <div class="url-tab">www.bedrockyield-holdings.com</div>
</section>

<!-- Outer spread: back cover -->
<section class="page outer-back">
  <svg class="shapes" width="560" height="725" viewBox="0 0 560 725">
    <polygon points="0,0 560,0 560,62 0,80" fill="var(--green)"/>
    <polygon points="0,80 560,62 560,470 0,490" fill="var(--charcoal)"/>
    <polygon points="0,490 560,470 560,478 0,498" fill="var(--green)"/>
    <path d="M150,110 A150,150 0 0 0 150,410" fill="none" stroke="var(--green-light)" stroke-width="20"/>
    <path d="M150,160 A100,100 0 0 0 150,360" fill="none" stroke="var(--green-pale)" stroke-width="4" opacity=".6"/>
  </svg>
  <p class="work-heading">How does the Bedrock Yield Private Holdings Scheme work?</p>
  <ol class="steps">
    <li class="step"><span class="step-icon"><svg width="18" height="18" viewBox="0 0 18 18"><circle cx="8" cy="8" r="5" fill="none" stroke="var(--green)" stroke-width="2"/><path d="M12 12l4 4" stroke="var(--green)" stroke-width="2"/></svg></span><div class="step-pill"><h4>Identify</h4><p>We screen producing royalty tracts across proven basins and pick those with steady output.</p></div></li>
    <li class="step"><span class="step-icon"><svg width="18" height="18" viewBox="0 0 18 18"><rect x="3" y="5" width="12" height="9" fill="none" stroke="var(--green)" stroke-width="2"/><path d="M6 5V3h6v2" stroke="var(--green)" stroke-width="2" fill="none"/></svg></span><div class="step-pill"><h4>Acquire</h4><p>Selected interests are bought at fair value and placed in your own private holding.</p></div></li>
    <li class="step"><span class="step-icon"><svg width="18" height="18" viewBox="0 0 18 18"><path d="M3 9l4 4 8-9" stroke="var(--green)" stroke-width="2" fill="none"/></svg></span><div class="step-pill"><h4>Manage</h4><p>Our team handles title, operator contact and monthly revenue checks on your behalf.</p></div></li>
    <li class="step"><span class="step-icon"><svg width="18" height="18" viewBox="0 0 18 18"><path d="M3 15h12M5 15V8M9 15V5M13 15V9" stroke="var(--green)" stroke-width="2"/></svg></span><div class="step-pill"><h4>Reinvestment</h4><p>Income may be rolled into new tracts to widen the holding over time.</p></div></li>
    <li class="step"><span class="step-icon"><svg width="18" height="18" viewBox="0 0 18 18"><path d="M2 14l5-5 3 3 6-7" stroke="var(--green)" stroke-width="2" fill="none"/></svg></span><div class="step-pill"><h4>Distribution</h4><p>Net royalty cash is paid to you each month with a clear, simple statement.</p></div></li>
  </ol>
  <div class="brand" style="left:30px;top:592px"><span class="brand-dot"></span><span class="brand-name">Bedrock<br>Yield, LLC</span></div>
  <ul class="contact">
    <li><svg viewBox="0 0 12 12"><rect width="12" height="12" rx="2" fill="var(--green)"/><path d="M4 3l1 2-1 1q1 2 2 2l1-1 2 1-1 2q-5-1-6-6z" fill="#fff"/></svg>(555) 214-7730</li>
    <li><svg viewBox="0 0 12 12"><rect width="12" height="12" rx="2" fill="var(--green)"/><path d="M2.5 4h7v5h-7zM2.5 4l3.5 3 3.5-3" stroke="#fff" fill="none"/></svg>hello@bedrockyield-holdings.com</li>
    <li><svg viewBox="0 0 12 12"><rect width="12" height="12" rx="2" fill="var(--green)"/><circle cx="6" cy="6" r="3.2" stroke="#fff" fill="none"/></svg>www.bedrockyield-holdings.com</li>
    <li><svg viewBox="0 0 12 12"><rect width="12" height="12" rx="2" fill="var(--green)"/><path d="M6 10S3 7 3 5a3 3 0 016 0c0 2-3 5-3 5z" fill="#fff"/></svg>4100 Quarry Lane, Suite 220, Fort Mesa, TX 75001</li>
  </ul>
</section>

<!-- Outer spread: front cover -->
<section class="page outer-front">
  <svg class="shapes" width="560" height="725" viewBox="0 0 560 725">
    <polygon points="0,0 560,0 560,92 0,118" fill="var(--green)"/>
    <polygon points="0,118 560,92 560,100 0,126" fill="var(--green-light)"/>
    <polygon points="0,552 560,545 560,552 0,562" fill="var(--green-light)"/>
    <path d="M0,562 L200,558 Q225,558 235,572 L0,578 Z" fill="var(--green)"/>
  </svg>
  <h1 class="title">Bedrock Yield Private Holdings Scheme</h1>
  <div class="photo photo-oilfield" role="img" aria-label="Photo of an oil pump jack in a dry field with snowy mountains under a blue sky"></div>
  <div class="brand" style="left:34px;top:630px"><span class="brand-dot"></span><span class="brand-name">Bedrock Yield, LLC</span></div>
  <div class="cover-note">
    <p>What should investors do in this uncertain period to profit from the evolving energy transition and protect themselves from what appears to be an inevitable wave of inflation?</p>
    <p>We have one asset class and a business opportunity that can address both.</p>
  </div>
  <div class="url-tab">www.bedrockyield-holdings.com</div>
</section>

<!-- Inner spread: left -->
<section class="page inner-left">
  <svg class="shapes" width="560" height="725" viewBox="0 0 560 725">
    <polygon points="0,0 560,0 560,232 0,250" fill="var(--charcoal-dark)"/>
    <polygon points="0,250 560,232 560,238 0,256" fill="var(--green)"/>
  </svg>
  <div class="lead">
    <h2>What should investors do in this uncertain period to profit from the evolving energy transition and protect themselves from what appears to be an inevitable wave of inflation?</h2>
    <h3>We have one asset class and a business opportunity that can address both.</h3>
    <p>Bedrock Yield is a family-run mineral and royalty firm that has bought producing interests for many years. We know the basins, the operators and the paperwork, and we have built a careful process to find tracts with long, steady output. Energy demand keeps rising while new supply stays tight, which supports prices. Royalty owners share in that income without paying drilling or operating costs, and the assets tend to rise in value when the dollar falls.</p>
  </div>
  <p class="intro">For the first time, we are opening this approach to a small number of private investors who want to own what we own. The scheme lets you hold real royalty interests in your own name, chosen and managed by our team, with clear monthly reporting.</p>
  <div class="col col-a">
    <div class="col-head">What are Personal Portfolios?</div>
    <ul class="bullets">
      <li>They are direct holdings of oil and gas royalty interests in your name.</li>
      <li>Each holding is spread across several wells and operators to limit risk.</li>
      <li>Tracts are chosen from the same pool we use for our own company.</li>
      <li>Income comes from producing wells, so cash flow can start quickly.</li>
      <li>Portfolios can be sized to suit a trust, family or retirement plan.</li>
    </ul>
  </div>
  <div class="col col-b">
    <div class="col-head">What owning a portfolio of energy royalties means for an investor?</div>
    <ul class="bullets">
      <li>A hard asset whose value tends to track energy prices and inflation.</li>
      <li>Monthly income with no share of drilling or operating costs.</li>
      <li>Possible tax benefits such as depletion allowance.</li>
      <li>The asset is real, can be passed on, and is held directly.</li>
    </ul>
  </div>
  <div class="photo photo-coins" role="img" aria-label="Illustration of gold coin stacks rising with small pump jacks on top"></div>
</section>

<!-- Inner spread: right -->
<section class="page inner-right">
  <div class="photo photo-markets" role="img" aria-label="Photo of gold and silver coin stacks with glasses on a financial chart"></div>
  <svg class="shapes" width="560" height="725" viewBox="0 0 560 725">
    <path d="M300,725 L300,690 Q300,672 320,672 L560,672 L560,725 Z" fill="var(--green)"/>
  </svg>
  <div class="brand" style="left:40px;top:262px"><span class="brand-dot"></span><span class="brand-name" style="font-size:16px">Bedrock Yield, LLC</span></div>
  <div class="why why-1">
    <h3>Why Bedrock Yield, LLC?</h3>
    <ul class="bullets">
      <li>We are a family firm that has bought and managed royalty interests for over fifteen years.</li>
      <li>Our team has reviewed thousands of tracts and keeps only a small share that meets our standards.</li>
      <li>We invest our own money alongside clients and hold the same kinds of assets.</li>
    </ul>
  </div>
  <div class="why why-2">
    <h3>Why did Bedrock Yield create the Private Holdings Scheme?</h3>
    <ul class="bullets">
      <li>Many people asked how they could own the same assets we buy, but deals are often too large for one person.</li>
      <li>By pooling our search and buying power, we can offer smaller tracts at fair prices to private buyers.</li>
      <li>The scheme gives investors a simple way to hold a hard asset with income and inflation protection.</li>
      <li>We take care of the details so owners can enjoy the monthly cash flow.</li>
    </ul>
  </div>
  <div class="url-tab" style="bottom:0;width:260px;height:53px;background:transparent">www.bedrockyield-holdings.com</div>
</section>

</body>
</html>
```